Letterhead Design Project

Letter head to include new logo and the following services:<br/><br/>Static Security, Mobile Patrols, Alarm Response & Key Holding, Alarm & CCTV Monitoring, Welfare Hire.<br/><br/>Phone: 0800 412 3968<br/>E-mail: security@tvr-holdings.example<br/><br/>Southern Office:<br/>TVR Security & Monitoring<br/>2nd Floor<br/>7 Pellingham Close<br/>London<br/>N9 4HX<br/><br/>Northern Office:<br/>TVR Security & Monitoring<br/>Crossway Nine Lorry Park<br/>Thornbury Lane<br/>Welby<br/>Sheffield<br/>S31 7QF<br/><br/>I need the files as PDF and an editable Microsoft Word Document. See attached file from my other business as an example. Do not copy information from uploaded word document, its just an example only. Logo also attached.<br/><br/><br/>SEE OTHER PROJECTS, THEY ARE ALL LINKED<br/> <br/>

```html
<!DOCTYPE html>
<html lang="en">
<head>
<meta charset="utf-8">
<title>TVR Security &amp; Monitoring — Letterhead</title>
<link href="https://fonts.googleapis.com/css2?family=Arimo:wght@700&family=Source+Sans+3:wght@400;600;700&display=swap" rel="stylesheet">
<style>
  :root {
    --brand-blue: #0b6fb9;
    --brand-dark: #242528;
    --paper: #f8f8f8;
    --backdrop: #e6e7e8;
    --body-text: #4a4a4a;
    --ink: #1c1c1c;
    --signature-tone: #d9d9d9;
  }
  * { box-sizing: border-box; margin: 0; padding: 0; }
  html, body {
    width: 1200px; height: 1200px; overflow: hidden;
    background: var(--backdrop);
  }
  .letterhead {
    position: absolute; left: 189px; top: 20px;
    width: 822px; height: 1160px;
    background: var(--paper);
    box-shadow: 0 2px 10px rgba(0,0,0,0.12);
    overflow: hidden;
    font-family: "Source Sans 3", "Myriad Pro", sans-serif;
  }
  .header-band {
    position: absolute; left: 0; top: 0; width: 822px; height: 140px;
    background: linear-gradient(100deg, #2b2c30 0%, #1d5f96 45%, var(--brand-blue) 70%);
  }

  .brand {
    position: absolute; left: 74px; top: 160px;
    display: flex; align-items: center; gap: 10px;
  }
  .brand-dot { width: 18px; height: 18px; border-radius: 50%; background: var(--brand-blue); flex: none; }
  .brand-name {
    font-size: 21px; font-weight: 700; line-height: 1.05;
    color: var(--brand-blue);
  }

  .services {
    position: absolute; left: 555px; top: 20px;
    list-style: none; color: #fff;
    font-size: 14.5px; line-height: 20.4px;
  }
  .services li { display: flex; align-items: center; gap: 7px; }
  .service-icon {
    width: 14px; height: 14px; border-radius: 50%; background: #fff; flex: none;
    display: flex; align-items: center; justify-content: center;
  }
  .service-icon::after {
    content: ""; width: 4px; height: 6px; border-radius: 2px; background: var(--brand-blue);
  }

  .greeting {
    position: absolute; left: 74px; top: 235px;
    font-family: "Arimo", Arial, sans-serif; font-weight: 700;
    font-size: 18px; color: var(--ink);
  }
  .letter-body {
    position: absolute; left: 74px; top: 281px; width: 674px;
    font-size: 17.4px; line-height: 21.6px; color: var(--body-text);
    text-align: justify;
  }
  .letter-body p + p { margin-top: 21.6px; }

  .signature {
    position: absolute; left: 74px; top: 846px; width: 129px; height: 62px;
    background: var(--signature-tone); border-radius: 4px;
  }

  .contact-footer {
    position: absolute; left: 74px; top: 1094px;
    border-left: 2px solid var(--brand-blue);
    padding-left: 10px;
    font-size: 12px; line-height: 20px; color: var(--ink);
  }
  .contact-row { display: flex; align-items: center; gap: 6px; white-space: nowrap; }
  .contact-item { display: inline-flex; align-items: center; gap: 4px; }
  .contact-item svg { width: 10px; height: 10px; fill: var(--brand-blue); }
  .contact-item + .contact-item { margin-left: 4px; }
  .office-label { color: var(--brand-blue); font-weight: 700; margin-right: 4px; }
</style>
</head>
<body>
<main class="letterhead">
  <div class="header-band" role="img" aria-label="Decorative blue and charcoal header wave"></div>

  <div class="brand">
    <span class="brand-dot"></span>
    <span class="brand-name">TVR Security<br>&amp; Monitoring</span>
  </div>

  <ul class="services">
    <li><span class="service-icon"></span>Static Security,</li>
    <li><span class="service-icon"></span>Mobile Patrols,</li>
    <li><span class="service-icon"></span>Alarm Response &amp; Key Holding,</li>
    <li><span class="service-icon"></span>Alarm &amp; CCTV Monitoring,</li>
    <li><span class="service-icon"></span>Welfare Hire.</li>
  </ul>

  <h1 class="greeting">Dear Mr. Hale,</h1>

  <section class="letter-body">
    <p>Lorem Ipsum is simply dummy text of the printing and typesetting industry. Lorem Ipsum has been the industry's standard dummy text ever since the 1500s, when an unknown printer took a galley of type and scrambled it to make a type specimen book. It has survived not only five centuries, but also the leap into electronic typesetting, remaining essentially unchanged.</p>
    <p>The standard chunk of Lorem Ipsum used since the 1500s is reproduced below for those interested. Sections 1.10.32 and 1.10.33 from "de Finibus Bonorum et Malorum" by Corvinus are also reproduced in their exact original form, accompanied by English versions from the 1914 translation by H. Pellow</p>
    <p>Lorem Ipsum is simply dummy text of the printing and typesetting industry. Lorem Ipsum has been the industry's standard dummy text ever since the 1500s, when an unknown printer took a galley of type and scrambled it to make a type specimen book. It has survived not only five centuries, but also the leap into electronic typesetting, remaining essentially unchanged. It was popularised in the</p>
    <p>The standard chunk of Lorem Ipsum used since the 1500s is reproduced below for those interested. Sections 1.10.32 and 1.10.33 from "de Finibus Bonorum et Malorum" by Corvinus are also reproduced in their exact original form, accompanied by English versions from the 1914 translation by H. Pellow</p>
    <p>The standard chunk of Lorem Ipsum used since the 1500s is reproduced below for those interested. Sections 1.10.32 and 1.10.33 from "de Finibus Bonorum et Malorum" by Corvinus are</p>
  </section>

  <div class="signature" role="img" aria-label="Handwritten signature of the sender"></div>

  <footer class="contact-footer">
    <div class="contact-row">
      <span class="contact-item">
        <svg viewBox="0 0 10 10" aria-hidden="true"><path d="M1,3 C1,1.5 2,1 5,1 C8,1 9,1.5 9,3 L7,3.5 L6.5,2.5 H3.5 L3,3.5 Z M2.5,4.5 H7.5 L8.5,9 H1.5 Z"/></svg>
        0800 412 3968
      </span>
      <span class="contact-item">
        <svg viewBox="0 0 10 10" aria-hidden="true"><path d="M0.5,2 H9.5 V8 H0.5 Z"/><path d="M0.5,2 L5,5.5 L9.5,2" fill="none" stroke="#fff" stroke-width="0.9"/></svg>
        security@tvr-holdings.example
      </span>
    </div>
    <div class="contact-row"><span class="office-label">Northern Office:-</span>Crossway Nine Lorry Park, Thornbury Lane, Welby, Sheffield, S31 7QF</div>
    <div class="contact-row"><span class="office-label">Southern Office:-</span>2nd Floor, 7 Pellingham Close, London, N9 4HX</div>
  </footer>
</main>
</body>
</html>
```